Brackwater Vale Medical Website to make connecting and communicating easier

To create a unique, user-friendly, professional website for patients and professionals to access education/ information, forms, appointments, contact details, and data about us, and for us to have the capacity to link to various cloud-based platforms.
To use the logo design and colour scheme we have just sourced.

WEBSITE to be eye catching, Inspiring and alluring
- efficient and logical
- professional and trustworthy appearance
- health focus "living health matters"
- user friendly
- ability to link with cloud-based software and video conferencing tools/ telehealth
- colours- black/ white teal and ?silver

PAGES:
page 1 - Our clinic and staff, services offered, contact us- address/ map / contact details- social media connections
page 2- patients and visitors - New patient forms to complete, news and patient informtion (educatinal)
page 3 - health professionals -referral forms, research and education
page 3- online appointments
page 4 - Quick links - partners, other services
page 5- privacy policy, disclaimer

Need extra days to review

HI, Could we please extend the deadline another 5 days, so sorry just struggling with my workload to be able to keep up and I am wanting to liaise more with the designer that I will choose. I am so happy with PixelForge and all the designers - thank you! Thank you so much!!

Target Market(s)

Patients - mostly over 60's so the website must be minimal clicks and simple to navigate
Professionals - for education and access forms

Industry/Entity Type

Health Care

Coding

Coded - Design and coding required

Number of Pages Required

5+ page

Font styles to use
Sans Serif
Script

Colors
33b8a4
86cfc6

Requirements
Must have
• WEBSITE to be eye catching, Inspiring and alluring
- efficient and logical
- user friendly

WEBSITE - professional and user friendly
- ability to link with cloud based software and videoconferencing/ telehealth
Nice to have
• clean and crisp presentation
happy for an innovative look
room to add more services and ability to link pages and resources
Should not have
• Please ensure the website is not:
clunky
difficult to navigate
common and cheap looking

```html
<!DOCTYPE html>
<html lang="en">
<head>
<meta charset="utf-8">
<title>Brackwater Vale Medical</title>
<link href="https://fonts.googleapis.com/css2?family=Montserrat:wght@500;600;700&family=Mulish:wght@400;600;700&display=swap" rel="stylesheet">
<style>
:root{
  --teal:#33b8a4;
  --teal-dark:#23857a;
  --teal-soft:#86cfc6;
  --teal-pale:#a4e6dc;
  --ink:#2b2b2b;
  --ink-head:#1f3d3a;
  --grey-bg:#f6f6f6;
  --muted:#666;
  --white:#fff;
}
*{margin:0;padding:0;box-sizing:border-box}
html,body{width:1200px;height:1200px;overflow:hidden;background:var(--white)}
body{font-family:"Mulish",sans-serif;color:var(--ink);position:relative}
.page{position:absolute;left:440px;top:0;width:320px;height:1200px;background:var(--white);overflow:hidden}
.abs{position:absolute}
.head{font-family:"Montserrat",sans-serif;font-weight:500;color:var(--ink-head)}
.rule{position:absolute;height:1.2px;width:16px;background:var(--teal-dark)}
.btn{position:absolute;border-radius:6px;background:var(--teal);color:var(--white);font-family:"Montserrat",sans-serif;font-size:2.6px;font-weight:600;letter-spacing:.15px;display:flex;align-items:center;justify-content:center}
.txt{font-size:2.7px;line-height:4px;color:#555}

/* header */
.topbar{left:0;top:0;width:320px;height:29px;background:var(--grey-bg)}
.brand{left:21px;top:9px;font-family:"Mulish",sans-serif;font-weight:700;font-size:4.4px;line-height:5px;color:var(--teal);width:40px}
.contact-mini{top:12.5px;font-size:2.8px;color:#333;display:flex;align-items:center;gap:2px;white-space:nowrap}
.nav{left:0;top:29px;width:320px;height:19px;background:var(--white)}
.nav span{position:absolute;top:7.5px;font-size:3.1px;color:#333;letter-spacing:.05px;white-space:nowrap}
.nav .active{color:var(--teal)}

/* hero */
.hero{left:0;top:48px;width:320px;height:152px;background:linear-gradient(100deg,#f1f5f6 0%,#e3eef1 40%,#c7e3ee 75%,#d8eaf2 100%)}
.hero-title{left:22px;top:80px;font-family:"Montserrat",sans-serif;font-weight:600;font-size:11.8px;line-height:12.2px;color:var(--ink-head)}
.hero-title em{font-style:normal;color:var(--teal-dark)}
.hero-sub{left:22px;top:110.5px;font-size:5px;color:#333;font-weight:600;white-space:nowrap}

/* info circles */
.circle{position:absolute;width:86px;height:84px;border-radius:50%;background:var(--teal-dark);box-shadow:0 2px 4px rgba(0,0,0,.12);color:var(--white);text-align:center}
.circle h3{position:absolute;left:0;right:0;top:26px;font-family:"Montserrat",sans-serif;font-weight:500;font-size:4.6px}
.circle p{position:absolute;left:9px;right:9px;top:35px;font-size:2.7px;line-height:4px}
.circle .ghost{position:absolute;left:20px;width:46px;top:57px;height:10px;border:.6px solid var(--white);border-radius:6px;font-size:2.6px;display:flex;align-items:center;justify-content:center}
.circle svg{position:absolute;left:38px;top:13px}

/* clinic */
.clinic-photo{left:21px;top:332px;width:128px;height:131px;border-radius:3px;background:linear-gradient(135deg,#e9f1f8 0%,#cddff0 55%,#b9cfe6 100%)}

/* services */
.services{left:0;top:488px;width:320px;height:193px;background:var(--teal-pale)}
.svc{position:absolute;width:58px}
.svc h4{font-size:3px;font-weight:600;color:#1d3533;margin-left:12px;letter-spacing:.05px;line-height:4px}
.svc p{font-size:2.7px;line-height:4px;color:#3a4a48;margin-left:12px;margin-top:2.5px}
.svc svg{position:absolute;left:0;top:-1px}

/* doctors */
.doctors{left:0;top:681px;width:320px;height:221px;background:var(--grey-bg)}
.card{position:absolute;width:64px;height:82px;background:var(--white);box-shadow:0 1px 3px rgba(0,0,0,.16);border-radius:1.5px;overflow:hidden;text-align:center}
.card .shot{height:58px;background:linear-gradient(180deg,#f4f6f8,#dfe6ec)}
.card h5{font-family:"Montserrat",sans-serif;font-weight:500;font-size:3.6px;color:#222;margin-top:6px}
.card small{display:block;font-size:2.4px;color:#777;margin-top:.6px;letter-spacing:.05px}
.card.hover .info{background:var(--teal-soft);height:24px}
.card.hover h5,.card.hover small{color:var(--white)}
.card.hover h5{padding-top:6px;margin-top:0}

/* testimonial */
.quote-band{left:0;top:902px;width:320px;height:86px;background:linear-gradient(90deg,#86d3c8 0%,#5ccbb9 55%,#33b8a4 100%)}
.dot{position:absolute;top:977px;width:2.2px;height:2.2px;border-radius:50%;background:rgba(255,255,255,.55)}

/* partners */
.partner{position:absolute;top:1052px;height:18px;border-radius:3px;background:#e7eceb}

/* footer */
.footer{left:0;top:1095px;width:320px;height:105px;background:var(--grey-bg)}
.fhead{position:absolute;font-size:3.3px;font-weight:600;color:#333;letter-spacing:.1px}
.flist{position:absolute;font-size:2.7px;color:#333;line-height:8.6px}
.fitem{position:absolute;font-size:2.7px;color:#333;line-height:4px;display:flex;gap:2px}
</style>
</head>
<body>
<div class="page">

  <!-- header -->
  <div class="abs topbar"></div>
  <div class="abs brand">Brackwater Vale Medical</div>
  <div class="abs contact-mini" style="left:215px">
    <svg width="4" height="3" viewBox="0 0 8 6"><rect x=".5" y=".5" width="7" height="5" fill="none" stroke="#33b8a4" stroke-width=".8"/><path d="M.5 .5 4 3.5 7.5 .5" fill="none" stroke="#33b8a4" stroke-width=".8"/></svg>
    info@bvmedical.com
  </div>
  <div class="abs contact-mini" style="left:263px">
    <svg width="3.5" height="3.5" viewBox="0 0 8 8"><path d="M1.5 .8 3 2.6 2.2 3.6c.6 1.2 1.3 1.9 2.3 2.3L5.4 5l1.8 1.5-.8 1.2C3.8 7.5.6 4.3.3 1.6Z" fill="none" stroke="#33b8a4" stroke-width=".7"/></svg>
    (800) 555-0148
  </div>

  <nav class="abs nav">
    <span class="active" style="left:21px">HOME</span>
    <span style="left:45px">ABOUT US</span>
    <span style="left:78px">OUR SERVICES</span>
    <span style="left:119px">PATIENTS &amp; VISITORS</span>
    <span style="left:172px">APPOINTMENTS</span>
    <span style="left:216px">NEWS &amp; INFORMATION</span>
    <span style="left:273px">CONTACT US</span>
  </nav>

  <!-- hero -->
  <div class="abs hero" role="img" aria-label="Photo of a smiling doctor with a stethoscope talking with an older patient"></div>
  <svg class="abs" style="left:0;top:48px" width="320" height="152" viewBox="0 0 320 152">
    <path d="M0 134C40 96 92 94 150 114C210 134 270 132 320 100L320 152L0 152Z" fill="#33b8a4"/>
  </svg>
  <h1 class="abs hero-title">We Care<br><em>For Your Health</em></h1>
  <div class="abs hero-sub">Experienced &amp; Compassionate Care</div>
  <div class="btn" style="left:22px;top:125px;width:60px;height:10px">Make An Appointment</div>

  <!-- info circles -->
  <div class="circle" style="left:22px;top:218px">
    <svg width="10" height="9" viewBox="0 0 10 9"><rect x="1.5" y="1" width="6" height="7" fill="none" stroke="#fff" stroke-width=".6"/><path d="M3 3h3M3 4.5h3M3 6h2M6 7.5 9 3" stroke="#fff" stroke-width=".6" fill="none"/></svg>
    <h3>Patient Forms</h3>
    <p>Lorem ipsum dolor sit amet, consetetur sadipscing elitr, sed diam nonumy eirmod tempor invidunt ut.</p>
    <div class="ghost">Go To Forms</div>
  </div>
  <div class="circle" style="left:117px;top:219px">
    <svg width="10" height="9" viewBox="0 0 10 9"><circle cx="5" cy="4.5" r="3.6" fill="none" stroke="#fff" stroke-width=".6"/><path d="M5 2.4v2.3l1.5 1" stroke="#fff" stroke-width=".6" fill="none"/></svg>
    <h3 style="top:25px">Office Hours</h3>
    <p style="top:35px;line-height:7.4px">Mondays, Wednesdays, &amp; Fridays<br>8:00 am - 5:00 pm<br><br>Tuesdays &amp; Thursdays<br>9:00 am - 6:00 pm</p>
  </div>
  <div class="circle" style="left:212px;top:218px">
    <svg width="10" height="9" viewBox="0 0 10 9"><rect x="1" y="1" width="8" height="7" fill="none" stroke="#fff" stroke-width=".6"/><path d="M5 1v7M6 3h2M6 4.5h2M6 6h2M2 6l2-2" stroke="#fff" stroke-width=".6" fill="none"/></svg>
    <h3 style="top:25px">Physician Referrals</h3>
    <p>Lorem ipsum dolor sit amet, consetetur sadipscing elitr, sed diam nonumy eirmod tempor invidunt ut.</p>
    <div class="ghost">Go To Referrals</div>
  </div>

  <!-- our clinic -->
  <div class="abs clinic-photo" role="img" aria-label="Photo of a doctor with a clipboard talking with a mother and her young son"></div>
  <h2 class="abs head" style="left:172px;top:357px;font-size:9.6px">Our Clinic</h2>
  <div class="rule" style="left:172px;top:372px"></div>
  <p class="abs" style="left:170px;top:376px;width:128px;font-size:3.8px;line-height:7.6px;color:var(--teal-dark)">Lorem ipsum dolor sit amet, consetetur sadipscing elitr, sed diam nonumy eirmod tempor invidunt ut.</p>
  <p class="abs txt" style="left:170px;top:397px;width:128px;line-height:6px">Lorem ipsum dolor sit amet, consetetur sadipscing elitr, sed diam nonumy eirmod tempor invidunt ut labore et dolore magna aliquyam erat, sed diam voluptua. At vero eos et accusam et justo duo dolores et ea rebum. Stet clita kasd.</p>
  <div class="btn" style="left:170px;top:427px;width:60px;height:11px">Learn More</div>

  <!-- services -->
  <div class="abs services"></div>
  <h2 class="abs head" style="left:21px;top:500px;font-size:9.6px">Our Services</h2>
  <div class="rule" style="left:21px;top:514px"></div>
  <div class="abs" style="left:21px;top:521px;font-size:4px;color:#333">Living Healthy Matters</div>
  <p class="abs txt" style="left:21px;top:529px;width:134px;line-height:6px;color:#3a4a48">Family Medicine provides the most variety of services to you as an individual or as a member of a family. From infancy to older adult and everything in between, being able to provide primary care services is a rewarding experience as a provider often following patients throughout their lifespan. It is more than just impacting your health...it is building a relationship and the essence of trust.</p>
  <p class="abs txt" style="left:168px;top:529px;width:136px;line-height:6px;color:#3a4a48">Health or homeostasis includes mind, body and spirit/soul. It is the integration of these parts that makes up health as a whole. We strive to treat the whole patient as a person....not just the disease. Your health care needs to be tailored to YOU and integrative care is apart of that.</p>

  <div class="svc" style="left:21px;top:583px">
    <svg width="8" height="8" viewBox="0 0 8 8"><path d="M1 1v2.5a2 2 0 0 0 4 0V1M3 5.5V7h3V5" fill="none" stroke="#23857a" stroke-width=".7"/></svg>
    <h4>WELLNESS CHECK-UPS</h4><p>Lorem ipsum dolor sit amet, consetetur sadipscing elitr,</p>
  </div>
  <div class="svc" style="left:92px;top:583.5px">
    <svg width="8" height="8" viewBox="0 0 8 8"><path d="M1 7 6 2M5 1l2 2M2.5 4.5l1 1" stroke="#23857a" stroke-width=".7" fill="none"/></svg>
    <h4>IMMUNIZATIONS</h4><p>Lorem ipsum dolor sit amet, consetetur sadipscing elitr,</p>
  </div>
  <div class="svc" style="left:163px;top:582px">
    <svg width="8" height="8" viewBox="0 0 8 8"><path d="M1.5 6.5 6 2M5 1l2 2M1 7l1-1" stroke="#23857a" stroke-width=".9" fill="none"/></svg>
    <h4>DIAGNOSTIC TESTING</h4><p>Lorem ipsum dolor sit amet, consetetur sadipscing elitr,</p>
  </div>
  <div class="svc" style="left:234px;top:581px;width:66px">
    <svg width="8" height="8" viewBox="0 0 8 8"><circle cx="4" cy="4.5" r="3" fill="none" stroke="#23857a" stroke-width=".7"/><path d="M4 1.5V.5" stroke="#23857a" stroke-width=".7"/></svg>
    <h4>NUTRITION GUIDANCE</h4><p>Lorem ipsum dolor sit amet, consetetur sadipscing elitr,<br><span style="font-weight:600;color:#1d3533">SPORTS MEDICINE</span></p>
    <p style="margin-top:2px">Lorem ipsum dolor sit amet, consetetur sadipscing elitr,</p>
  </div>
  <div class="svc" style="left:22px;top:618px;width:60px">
    <svg width="8" height="8" viewBox="0 0 8 8"><circle cx="3.2" cy="4.8" r="2" fill="none" stroke="#23857a" stroke-width=".7"/><path d="M4.6 3.4 7 1M5 1h2v2" stroke="#23857a" stroke-width=".7" fill="none"/></svg>
    <h4>MEN'S HEALTH</h4><p>Lorem ipsum dolor sit amet, consetetur sadipscing elitr, sed diam</p>
  </div>
  <div class="svc" style="left:92px;top:617px">
    <svg width="8" height="8" viewBox="0 0 8 8"><circle cx="4" cy="3" r="2" fill="none" stroke="#23857a" stroke-width=".7"/><path d="M4 5v3M2.8 6.6h2.4" stroke="#23857a" stroke-width=".7"/></svg>
    <h4>WOMEN'S HEALTH</h4><p>Lorem ipsum dolor sit amet, consetetur sadipscing elitr,</p>
  </div>
  <div class="svc" style="left:163px;top:615px;width:62px">
    <svg width="8" height="8" viewBox="0 0 8 8"><path d="M4 .5v7.5M1 2.5h6M2.5 4.5h3" stroke="#23857a" stroke-width=".7"/></svg>
    <h4>CHRONIC &amp; ACUTE ADULT ILLNESSES</h4><p>Lorem ipsum dolor sit amet, consetetur sadipscing elitr,</p>
  </div>

  <div class="btn" style="left:125px;top:654px;width:60px;height:10px">Explore Services</div>

  <!-- doctors -->
  <div class="abs doctors"></div>
  <h2 class="abs head" style="left:0;width:320px;text-align:center;top:696px;font-size:9.6px">Our Doctors</h2>
  <div class="rule" style="left:129px;top:709px"></div>
  <p class="abs" style="left:92px;top:718px;width:130px;font-size:2.9px;line-height:6px;color:var(--teal-dark)">Click on doctors profile to see more info. First item shows interaction when user hovers over card profile.</p>
  <p class="abs txt" style="left:93px;top:737px;width:130px;line-height:6px">But I must explain to you how all this mistaken idea of denouncing pleasure and praising pain was born and I will give you a complete account of the system, and expound the actual teachings of the great explorer of the truth, the master-builder of human happiness.</p>

  <div class="card" style="left:50px;top:774px">
    <div class="shot" role="img" aria-label="Portrait photo of a male doctor in a white coat"></div>
    <h5>Marcus Reid, M.D.</h5><small>OBSTETRICS &amp; GYNECOLOGY</small>
  </div>
  <div class="card hover" style="left:123px;top:772px">
    <div class="shot" role="img" aria-label="Portrait photo of a female doctor in a white coat"></div>
    <div class="info"><h5>Clara Whitfield, M.D.</h5><small>FAMILY MEDICINE</small></div>
  </div>
  <div class="card" style="left:195px;top:772px">
    <div class="shot" role="img" aria-label="Portrait photo of a smiling male doctor with a stethoscope"></div>
    <h5>Marcus Reid, M.D.</h5><small>INTERNAL MEDICINE</small>
  </div>
  <div class="btn" style="left:130px;top:866px;width:60px;height:10px">Meet Our Team</div>

  <!-- testimonial -->
  <div class="abs quote-band"></div>
  <svg class="abs" style="left:154px;top:914px" width="12" height="8" viewBox="0 0 12 8">
    <path d="M1 6a2.5 2.5 0 1 1 4-2C5 6 3.5 7.5 1.5 8ZM7 6a2.5 2.5 0 1 1 4-2c0 2-1.5 3.5-3.5 4Z" fill="#23857a"/>
  </svg>
  <p class="abs" style="left:90px;top:930.5px;width:140px;text-align:center;font-size:2.9px;line-height:6px;color:#fff">Thank you for the care I received from both the nursing staff and the doctors. Their skills and knowledge are truly exceptional.</p>
  <div class="abs" style="left:142px;top:949px;width:11px;height:11px;border-radius:50%;background:linear-gradient(135deg,#f1d9c4,#c79e7e)" role="img" aria-label="Small portrait of the patient"></div>
  <div class="abs" style="left:159px;top:953px;font-size:2.8px;color:#fff">R.T. Hollis</div>
  <span class="dot" style="left:151px;background:#fff"></span>
  <span class="dot" style="left:156px"></span>
  <span class="dot" style="left:161px"></span>
  <span class="dot" style="left:166px"></span>

  <!-- partners -->
  <h2 class="abs head" style="left:0;width:320px;text-align:center;top:1011px;font-size:9.6px">Our Partners</h2>
  <div class="rule" style="left:127px;top:1025px"></div>
  <div class="partner" style="left:21px;width:35px;top:1055px;height:12px"></div>
  <div class="partner" style="left:75px;width:29px;top:1046px;height:30px"></div>
  <div class="partner" style="left:123px;width:31px;top:1054px;height:14px"></div>
  <div class="partner" style="left:174px;width:32px;top:1051px;height:20px;border-radius:50%"></div>
  <div class="partner" style="left:226px;width:73px;top:1053px;height:14px"></div>

  <!-- footer -->
  <div class="abs footer"></div>
  <div class="abs brand" style="top:1114px;width:40px">Brackwater Vale Medical</div>

  <div class="fhead" style="left:109px;top:1111px">CONTACT</div>
  <div class="fitem" style="left:103px;top:1122px">
    <svg width="3" height="4" viewBox="0 0 6 8"><path d="M3 7.5S.5 4.5.5 3a2.5 2.5 0 0 1 5 0C5.5 4.5 3 7.5 3 7.5Z" fill="none" stroke="#33b8a4" stroke-width=".7"/></svg>
    <span>1234 Harbour Rd.<br>Brackwater, QL 4021</span>
  </div>
  <div class="fitem" style="left:103px;top:1140px">
    <svg width="4" height="3" viewBox="0 0 8 6"><rect x=".5" y=".5" width="7" height="5" fill="none" stroke="#33b8a4" stroke-width=".8"/><path d="M.5 .5 4 3.5 7.5 .5" fill="none" stroke="#33b8a4" stroke-width=".8"/></svg>
    <span>care@bvmedical.com</span>
  </div>
  <div class="fitem" style="left:103px;top:1152px">
    <svg width="3.5" height="3.5" viewBox="0 0 8 8"><path d="M1.5 .8 3 2.6 2.2 3.6c.6 1.2 1.3 1.9 2.3 2.3L5.4 5l1.8 1.5-.8 1.2C3.8 7.5.6 4.3.3 1.6Z" fill="none" stroke="#33b8a4" stroke-width=".7"/></svg>
    <span>(345)555-0162</span>
  </div>

  <div class="fhead" style="left:199px;top:1111px">MENU</div>
  <div class="flist" style="left:200px;top:1118px">About Us<br>Our Services<br>Patients &amp; Visitors<br>Appointments<br>News &amp; Information<br>Contact Us</div>

  <div class="fhead" style="left:274px;top:1112px">FOLLOW US</div>
  <div class="flist" style="left:274.5px;top:1117px">Friendface<br>Chirper<br>Snapgram<br>Searchplus<br>Viewtube</div>

  <div class="abs" style="left:21px;top:1180px;width:278px;height:.5px;background:#d4d4d4"></div>
  <div class="abs" style="left:0;width:320px;text-align:center;top:1187px;font-size:2.3px;color:#555">©2020 Brackwater Vale Medical. All Rights Reserved. &nbsp;&nbsp; <span style="color:var(--teal);text-decoration:underline">Disclaimer</span> | <span style="color:var(--teal);text-decoration:underline">Privacy Policy</span></div>

</div>
</body>
</html>
```